Graphic background for 10 Pull Up Banners

To produce a graphic background for a 100 cm wide by 200 cm high Pull-Up Display banner containing a Buddhist text in three languages: Tibetan, Mandarin and English. Please refer to uploaded file "Elements of Pull Up Banner". The design should be simple (not drawing attention away from the text). This design should then be varied for or extended to the next banner and so on until the 10th banner. When the banners are lined up, they should form a single design that is 1000 cm wide by 200 cm high.
An alternative way to look at the project is to produce a graphic background of 1000 cm width by 200 cm height that is then splitted into ten separate 100 cm wide by 200 cm high graphic to be used as background for 10 Buddhist texts (text 1, 2, 3, 4, 5, 6, 7, 8, 9a, 9b) on 10 Pull-Up Display Banners, the text in each banner being in the three languages mentioned earlier.
In either perspective, the design should be simple and not draw attention away from the texts. See uploaded PDF file "Examples.pdf"
For attendees at a Buddhist Event.

```html
<!DOCTYPE html>
<html lang="en">
<head>
<meta charset="utf-8">
<title>Ten Mistaking – Pull-Up Banner Series</title>
<link href="https://fonts.googleapis.com/css2?family=Questrial&family=Noto+Sans+SC:wght@400;700&family=Noto+Sans+Tibetan&display=swap" rel="stylesheet">
<style>
  :root {
    --page: #ffffff;
    --header-white: #fdfcf8;
    --maroon: #7a1411;
    --title-cream: #ffe9b0;
    --orange-light: #ffd25a;
    --orange-mid: #f7a81c;
    --orange-deep: #ee7a14;
    --panel: rgba(255, 236, 150, 0.45);
    --footer-brown: #6b3208;
    --footer-text: #ffe7b8;
    --body-text: #4a2206;
    --shadow: rgba(0, 0, 0, 0.28);
  }
  * { box-sizing: border-box; margin: 0; padding: 0; }
  html, body {
    width: 1200px; height: 262px; overflow: hidden; background: var(--page);
  }
  .banner-row { position: relative; width: 1200px; height: 262px; }
  .banner {
    position: absolute; top: 28px; width: 108px; height: 212px;
    background: var(--header-white);
    box-shadow: 1px 2px 4px var(--shadow);
    overflow: hidden;
  }
  .banner:nth-child(1)  { left: 15px; }
  .banner:nth-child(2)  { left: 133px; }
  .banner:nth-child(3)  { left: 251px; }
  .banner:nth-child(4)  { left: 369px; }
  .banner:nth-child(5)  { left: 487px; }
  .banner:nth-child(6)  { left: 605px; }
  .banner:nth-child(7)  { left: 723px; }
  .banner:nth-child(8)  { left: 841px; }
  .banner:nth-child(9)  { left: 959px; }
  .banner:nth-child(10) { left: 1077px; }

  /* one continuous field running across all ten banners */
  .banner-field {
    position: absolute; left: 0; top: 30px; width: 108px; height: 156px;
    background:
      radial-gradient(ellipse 70px 40px at 60px 60px, rgba(238,110,20,.55), transparent 70%),
      radial-gradient(ellipse 60px 50px at 300px 95px, rgba(235,100,20,.6), transparent 70%),
      radial-gradient(ellipse 50px 60px at 460px 110px, rgba(236,96,18,.6), transparent 70%),
      radial-gradient(ellipse 80px 30px at 620px 40px, rgba(240,120,20,.45), transparent 70%),
      radial-gradient(ellipse 70px 40px at 820px 120px, rgba(240,110,20,.45), transparent 70%),
      radial-gradient(ellipse 90px 40px at 1100px 100px, rgba(238,110,20,.5), transparent 70%),
      linear-gradient(180deg, var(--orange-light) 0%, var(--orange-mid) 55%, var(--orange-deep) 100%);
    background-size: 1200px 156px;
  }
  .banner:nth-child(1)  .banner-field { background-position: -15px 0; }
  .banner:nth-child(2)  .banner-field { background-position: -133px 0; }
  .banner:nth-child(3)  .banner-field { background-position: -251px 0; }
  .banner:nth-child(4)  .banner-field { background-position: -369px 0; }
  .banner:nth-child(5)  .banner-field { background-position: -487px 0; }
  .banner:nth-child(6)  .banner-field { background-position: -605px 0; }
  .banner:nth-child(7)  .banner-field { background-position: -723px 0; }
  .banner:nth-child(8)  .banner-field { background-position: -841px 0; }
  .banner:nth-child(9)  .banner-field { background-position: -959px 0; }
  .banner:nth-child(10) .banner-field { background-position: -1077px 0; }

  .text-panel {
    position: absolute; left: 10px; top: 46px; width: 88px; height: 136px;
    background: var(--panel); border-radius: 3px;
  }
  .header-tab { position: absolute; left: 38px; top: 0; width: 70px; height: 44px; }
  .org-name {
    position: absolute; left: 3px; top: 8px; width: 34px;
    font: 400 5px/1.2 "Questrial", sans-serif; color: var(--maroon);
    text-align: center; white-space: nowrap;
  }
  .org-name::before {
    content: ""; display: block; width: 10px; height: 10px; margin: 0 auto 3px;
    border-radius: 50%; background: var(--maroon);
  }
  .title-zh {
    position: absolute; left: 46px; top: 6px;
    font: 700 8.5px/1 "Noto Sans SC", sans-serif; color: var(--title-cream);
  }
  .title-en {
    position: absolute; left: 46px; top: 17px;
    font: 400 7.5px/1 "Questrial", sans-serif; color: var(--title-cream);
  }
  .verse { position: absolute; color: var(--body-text); white-space: nowrap; }
  .verse p { font-size: 2.4px; line-height: 4.4px; }
  .verse-tibetan { left: 36px; top: 50px; font-family: "Noto Sans Tibetan", sans-serif; }
  .verse-chinese { left: 36px; top: 94px; font-family: "Noto Sans SC", sans-serif; }
  .verse-chinese p { line-height: 3.8px; }
  .verse-notes { left: 38px; top: 124px; font-family: "Noto Sans SC", sans-serif; }
  .verse-notes p { line-height: 3.6px; }
  .verse-english { left: 13px; top: 141px; font-family: "Questrial", sans-serif; }
  .verse-english p { font-size: 2.2px; line-height: 4.2px; }

  .footer-band {
    position: absolute; left: 0; bottom: 0; width: 108px; height: 26px;
    background: var(--footer-brown); color: var(--footer-text);
    font-family: "Questrial", sans-serif;
  }
  .footer-web { position: absolute; left: 0; width: 108px; top: 5px; text-align: center; font-size: 3.6px; }
  .footer-zh { position: absolute; left: 0; width: 108px; top: 11px; text-align: center; font: 2.4px/1 "Noto Sans SC", sans-serif; }
  .footer-tagline { position: absolute; left: 0; width: 108px; top: 17px; text-align: center; font-size: 2.4px; }
</style>
</head>
<body>
<main class="banner-row">

<section class="banner">
  <div class="banner-field"></div>
  <div class="text-panel"></div>
  <svg class="header-tab" viewBox="0 0 70 44" aria-hidden="true"><polygon points="0,0 70,0 70,30 36,30 24,42 12,30 0,30" fill="var(--maroon)"/></svg>
  <div class="org-name">Lotus Garden</div>
  <h1 class="title-zh">十个口解</h1><h2 class="title-en">Ten Mistaking</h2>
  <div class="verse verse-tibetan"><p>ཆོས་ཀྱི་སྒོ་འབྱེད་པ།</p><p>སེམས་ཅན་ཀུན་ལ་བྱམས།</p><p>བློ་སྦྱོང་ཚིག་བཅད་པ།</p><p>ཞི་བའི་ལམ་ལ་འཇུག</p><p>བརྩོན་འགྲུས་རྟག་ཏུ་བསྐྱེད།</p><p>དགེ་བ་ཀུན་ལ་བསྔོ།</p></div>
  <div class="verse verse-chinese"><p>心念安住于正道中</p><p>善言开启众生之门</p><p>错误见解应当放下</p><p>耐心倾听慈悲增长</p><p>明见带来日常安宁</p><p>精进不懈远离骄慢</p><p>思维而后方可行事</p></div>
  <div class="verse verse-notes"><p>一、心念清净不散乱</p><p>二、功德回向一切众生</p></div>
  <div class="verse verse-english"><p>Mind at ease we walk the path today.</p><p>Kind words open the door to others.</p><p>Each mistaken view may be gently set aside.</p><p>Patience grows when we listen with care.</p><p>Clear seeing brings calm to daily life.</p><p>Let effort be steady and free of pride.</p><p>Study and reflect before we choose to act.</p><p>Share the merit with every living being.</p></div>
  <footer class="footer-band"><p class="footer-web">www.lotusgarden-centre.org</p><p class="footer-zh">莲花园共修</p><p class="footer-tagline">May all beings find peace together</p></footer>
</section>

<section class="banner">
  <div class="banner-field"></div>
  <div class="text-panel"></div>
  <svg class="header-tab" viewBox="0 0 70 44" aria-hidden="true"><polygon points="0,0 70,0 70,30 36,30 24,42 12,30 0,30" fill="var(--maroon)"/></svg>
  <div class="org-name">Lotus Garden</div>
  <h1 class="title-zh">十个口解</h1><h2 class="title-en">Ten Mistaking</h2>
  <div class="verse verse-tibetan"><p>ཆོས་ཀྱི་སྒོ་འབྱེད་པ།</p><p>སེམས་ཅན་ཀུན་ལ་བྱམས།</p><p>བློ་སྦྱོང་ཚིག་བཅད་པ།</p><p>ཞི་བའི་ལམ་ལ་འཇུག</p><p>བརྩོན་འགྲུས་རྟག་ཏུ་བསྐྱེད།</p><p>དགེ་བ་ཀུན་ལ་བསྔོ།</p></div>
  <div class="verse verse-chinese"><p>心念安住于正道中</p><p>善言开启众生之门</p><p>错误见解应当放下</p><p>耐心倾听慈悲增长</p><p>明见带来日常安宁</p><p>精进不懈远离骄慢</p><p>思维而后方可行事</p></div>
  <div class="verse verse-notes"><p>一、心念清净不散乱</p><p>二、功德回向一切众生</p></div>
  <div class="verse verse-english"><p>Mind at ease we walk the path today.</p><p>Kind words open the door to others.</p><p>Each mistaken view may be gently set aside.</p><p>Patience grows when we listen with care.</p><p>Clear seeing brings calm to daily life.</p><p>Let effort be steady and free of pride.</p><p>Study and reflect before we choose to act.</p><p>Share the merit with every living being.</p></div>
  <footer class="footer-band"><p class="footer-web">www.lotusgarden-centre.org</p><p class="footer-zh">莲花园共修</p><p class="footer-tagline">May all beings find peace together</p></footer>
</section>

<section class="banner">
  <div class="banner-field"></div>
  <div class="text-panel"></div>
  <svg class="header-tab" viewBox="0 0 70 44" aria-hidden="true"><polygon points="0,0 70,0 70,30 36,30 24,42 12,30 0,30" fill="var(--maroon)"/></svg>
  <div class="org-name">Lotus Garden</div>
  <h1 class="title-zh">十个口解</h1><h2 class="title-en">Ten Mistaking</h2>
  <div class="verse verse-tibetan"><p>ཆོས་ཀྱི་སྒོ་འབྱེད་པ།</p><p>སེམས་ཅན་ཀུན་ལ་བྱམས།</p><p>བློ་སྦྱོང་ཚིག་བཅད་པ།</p><p>ཞི་བའི་ལམ་ལ་འཇུག</p><p>བརྩོན་འགྲུས་རྟག་ཏུ་བསྐྱེད།</p><p>དགེ་བ་ཀུན་ལ་བསྔོ།</p></div>
  <div class="verse verse-chinese"><p>心念安住于正道中</p><p>善言开启众生之门</p><p>错误见解应当放下</p><p>耐心倾听慈悲增长</p><p>明见带来日常安宁</p><p>精进不懈远离骄慢</p><p>思维而后方可行事</p></div>
  <div class="verse verse-notes"><p>一、心念清净不散乱</p><p>二、功德回向一切众生</p></div>
  <div class="verse verse-english"><p>Mind at ease we walk the path today.</p><p>Kind words open the door to others.</p><p>Each mistaken view may be gently set aside.</p><p>Patience grows when we listen with care.</p><p>Clear seeing brings calm to daily life.</p><p>Let effort be steady and free of pride.</p><p>Study and reflect before we choose to act.</p><p>Share the merit with every living being.</p></div>
  <footer class="footer-band"><p class="footer-web">www.lotusgarden-centre.org</p><p class="footer-zh">莲花园共修</p><p class="footer-tagline">May all beings find peace together</p></footer>
</section>

<section class="banner">
  <div class="banner-field"></div>
  <div class="text-panel"></div>
  <svg class="header-tab" viewBox="0 0 70 44" aria-hidden="true"><polygon points="0,0 70,0 70,30 36,30 24,42 12,30 0,30" fill="var(--maroon)"/></svg>
  <div class="org-name">Lotus Garden</div>
  <h1 class="title-zh">十个口解</h1><h2 class="title-en">Ten Mistaking</h2>
  <div class="verse verse-tibetan"><p>ཆོས་ཀྱི་སྒོ་འབྱེད་པ།</p><p>སེམས་ཅན་ཀུན་ལ་བྱམས།</p><p>བློ་སྦྱོང་ཚིག་བཅད་པ།</p><p>ཞི་བའི་ལམ་ལ་འཇུག</p><p>བརྩོན་འགྲུས་རྟག་ཏུ་བསྐྱེད།</p><p>དགེ་བ་ཀུན་ལ་བསྔོ།</p></div>
  <div class="verse verse-chinese"><p>心念安住于正道中</p><p>善言开启众生之门</p><p>错误见解应当放下</p><p>耐心倾听慈悲增长</p><p>明见带来日常安宁</p><p>精进不懈远离骄慢</p><p>思维而后方可行事</p></div>
  <div class="verse verse-notes"><p>一、心念清净不散乱</p><p>二、功德回向一切众生</p></div>
  <div class="verse verse-english"><p>Mind at ease we walk the path today.</p><p>Kind words open the door to others.</p><p>Each mistaken view may be gently set aside.</p><p>Patience grows when we listen with care.</p><p>Clear seeing brings calm to daily life.</p><p>Let effort be steady and free of pride.</p><p>Study and reflect before we choose to act.</p><p>Share the merit with every living being.</p></div>
  <footer class="footer-band"><p class="footer-web">www.lotusgarden-centre.org</p><p class="footer-zh">莲花园共修</p><p class="footer-tagline">May all beings find peace together</p></footer>
</section>

<section class="banner">
  <div class="banner-field"></div>
  <div class="text-panel"></div>
  <svg class="header-tab" viewBox="0 0 70 44" aria-hidden="true"><polygon points="0,0 70,0 70,30 36,30 24,42 12,30 0,30" fill="var(--maroon)"/></svg>
  <div class="org-name">Lotus Garden</div>
  <h1 class="title-zh">十个口解</h1><h2 class="title-en">Ten Mistaking</h2>
  <div class="verse verse-tibetan"><p>ཆོས་ཀྱི་སྒོ་འབྱེད་པ།</p><p>སེམས་ཅན་ཀུན་ལ་བྱམས།</p><p>བློ་སྦྱོང་ཚིག་བཅད་པ།</p><p>ཞི་བའི་ལམ་ལ་འཇུག</p><p>བརྩོན་འགྲུས་རྟག་ཏུ་བསྐྱེད།</p><p>དགེ་བ་ཀུན་ལ་བསྔོ།</p></div>
  <div class="verse verse-chinese"><p>心念安住于正道中</p><p>善言开启众生之门</p><p>错误见解应当放下</p><p>耐心倾听慈悲增长</p><p>明见带来日常安宁</p><p>精进不懈远离骄慢</p><p>思维而后方可行事</p></div>
  <div class="verse verse-notes"><p>一、心念清净不散乱</p><p>二、功德回向一切众生</p></div>
  <div class="verse verse-english"><p>Mind at ease we walk the path today.</p><p>Kind words open the door to others.</p><p>Each mistaken view may be gently set aside.</p><p>Patience grows when we listen with care.</p><p>Clear seeing brings calm to daily life.</p><p>Let effort be steady and free of pride.</p><p>Study and reflect before we choose to act.</p><p>Share the merit with every living being.</p></div>
  <footer class="footer-band"><p class="footer-web">www.lotusgarden-centre.org</p><p class="footer-zh">莲花园共修</p><p class="footer-tagline">May all beings find peace together</p></footer>
</section>

<section class="banner">
  <div class="banner-field"></div>
  <div class="text-panel"></div>
  <svg class="header-tab" viewBox="0 0 70 44" aria-hidden="true"><polygon points="0,0 70,0 70,30 36,30 24,42 12,30 0,30" fill="var(--maroon)"/></svg>
  <div class="org-name">Lotus Garden</div>
  <h1 class="title-zh">十个口解</h1><h2 class="title-en">Ten Mistaking</h2>
  <div class="verse verse-tibetan"><p>ཆོས་ཀྱི་སྒོ་འབྱེད་པ།</p><p>སེམས་ཅན་ཀུན་ལ་བྱམས།</p><p>བློ་སྦྱོང་ཚིག་བཅད་པ།</p><p>ཞི་བའི་ལམ་ལ་འཇུག</p><p>བརྩོན་འགྲུས་རྟག་ཏུ་བསྐྱེད།</p><p>དགེ་བ་ཀུན་ལ་བསྔོ།</p></div>
  <div class="verse verse-chinese"><p>心念安住于正道中</p><p>善言开启众生之门</p><p>错误见解应当放下</p><p>耐心倾听慈悲增长</p><p>明见带来日常安宁</p><p>精进不懈远离骄慢</p><p>思维而后方可行事</p></div>
  <div class="verse verse-notes"><p>一、心念清净不散乱</p><p>二、功德回向一切众生</p></div>
  <div class="verse verse-english"><p>Mind at ease we walk the path today.</p><p>Kind words open the door to others.</p><p>Each mistaken view may be gently set aside.</p><p>Patience grows when we listen with care.</p><p>Clear seeing brings calm to daily life.</p><p>Let effort be steady and free of pride.</p><p>Study and reflect before we choose to act.</p><p>Share the merit with every living being.</p></div>
  <footer class="footer-band"><p class="footer-web">www.lotusgarden-centre.org</p><p class="footer-zh">莲花园共修</p><p class="footer-tagline">May all beings find peace together</p></footer>
</section>

<section class="banner">
  <div class="banner-field"></div>
  <div class="text-panel"></div>
  <svg class="header-tab" viewBox="0 0 70 44" aria-hidden="true"><polygon points="0,0 70,0 70,30 36,30 24,42 12,30 0,30" fill="var(--maroon)"/></svg>
  <div class="org-name">Lotus Garden</div>
  <h1 class="title-zh">十个口解</h1><h2 class="title-en">Ten Mistaking</h2>
  <div class="verse verse-tibetan"><p>ཆོས་ཀྱི་སྒོ་འབྱེད་པ།</p><p>སེམས་ཅན་ཀུན་ལ་བྱམས།</p><p>བློ་སྦྱོང་ཚིག་བཅད་པ།</p><p>ཞི་བའི་ལམ་ལ་འཇུག</p><p>བརྩོན་འགྲུས་རྟག་ཏུ་བསྐྱེད།</p><p>དགེ་བ་ཀུན་ལ་བསྔོ།</p></div>
  <div class="verse verse-chinese"><p>心念安住于正道中</p><p>善言开启众生之门</p><p>错误见解应当放下</p><p>耐心倾听慈悲增长</p><p>明见带来日常安宁</p><p>精进不懈远离骄慢</p><p>思维而后方可行事</p></div>
  <div class="verse verse-notes"><p>一、心念清净不散乱</p><p>二、功德回向一切众生</p></div>
  <div class="verse verse-english"><p>Mind at ease we walk the path today.</p><p>Kind words open the door to others.</p><p>Each mistaken view may be gently set aside.</p><p>Patience grows when we listen with care.</p><p>Clear seeing brings calm to daily life.</p><p>Let effort be steady and free of pride.</p><p>Study and reflect before we choose to act.</p><p>Share the merit with every living being.</p></div>
  <footer class="footer-band"><p class="footer-web">www.lotusgarden-centre.org</p><p class="footer-zh">莲花园共修</p><p class="footer-tagline">May all beings find peace together</p></footer>
</section>

<section class="banner">
  <div class="banner-field"></div>
  <div class="text-panel"></div>
  <svg class="header-tab" viewBox="0 0 70 44" aria-hidden="true"><polygon points="0,0 70,0 70,30 36,30 24,42 12,30 0,30" fill="var(--maroon)"/></svg>
  <div class="org-name">Lotus Garden</div>
  <h1 class="title-zh">十个口解</h1><h2 class="title-en">Ten Mistaking</h2>
  <div class="verse verse-tibetan"><p>ཆོས་ཀྱི་སྒོ་འབྱེད་པ།</p><p>སེམས་ཅན་ཀུན་ལ་བྱམས།</p><p>བློ་སྦྱོང་ཚིག་བཅད་པ།</p><p>ཞི་བའི་ལམ་ལ་འཇུག</p><p>བརྩོན་འགྲུས་རྟག་ཏུ་བསྐྱེད།</p><p>དགེ་བ་ཀུན་ལ་བསྔོ།</p></div>
  <div class="verse verse-chinese"><p>心念安住于正道中</p><p>善言开启众生之门</p><p>错误见解应当放下</p><p>耐心倾听慈悲增长</p><p>明见带来日常安宁</p><p>精进不懈远离骄慢</p><p>思维而后方可行事</p></div>
  <div class="verse verse-notes"><p>一、心念清净不散乱</p><p>二、功德回向一切众生</p></div>
  <div class="verse verse-english"><p>Mind at ease we walk the path today.</p><p>Kind words open the door to others.</p><p>Each mistaken view may be gently set aside.</p><p>Patience grows when we listen with care.</p><p>Clear seeing brings calm to daily life.</p><p>Let effort be steady and free of pride.</p><p>Study and reflect before we choose to act.</p><p>Share the merit with every living being.</p></div>
  <footer class="footer-band"><p class="footer-web">www.lotusgarden-centre.org</p><p class="footer-zh">莲花园共修</p><p class="footer-tagline">May all beings find peace together</p></footer>
</section>

<section class="banner">
  <div class="banner-field"></div>
  <div class="text-panel"></div>
  <svg class="header-tab" viewBox="0 0 70 44" aria-hidden="true"><polygon points="0,0 70,0 70,30 36,30 24,42 12,30 0,30" fill="var(--maroon)"/></svg>
  <div class="org-name">Lotus Garden</div>
  <h1 class="title-zh">十个口解</h1><h2 class="title-en">Ten Mistaking</h2>
  <div class="verse verse-tibetan"><p>ཆོས་ཀྱི་སྒོ་འབྱེད་པ།</p><p>སེམས་ཅན་ཀུན་ལ་བྱམས།</p><p>བློ་སྦྱོང་ཚིག་བཅད་པ།</p><p>ཞི་བའི་ལམ་ལ་འཇུག</p><p>བརྩོན་འགྲུས་རྟག་ཏུ་བསྐྱེད།</p><p>དགེ་བ་ཀུན་ལ་བསྔོ།</p></div>
  <div class="verse verse-chinese"><p>心念安住于正道中</p><p>善言开启众生之门</p><p>错误见解应当放下</p><p>耐心倾听慈悲增长</p><p>明见带来日常安宁</p><p>精进不懈远离骄慢</p><p>思维而后方可行事</p></div>
  <div class="verse verse-notes"><p>一、心念清净不散乱</p><p>二、功德回向一切众生</p></div>
  <div class="verse verse-english"><p>Mind at ease we walk the path today.</p><p>Kind words open the door to others.</p><p>Each mistaken view may be gently set aside.</p><p>Patience grows when we listen with care.</p><p>Clear seeing brings calm to daily life.</p><p>Let effort be steady and free of pride.</p><p>Study and reflect before we choose to act.</p><p>Share the merit with every living being.</p></div>
  <footer class="footer-band"><p class="footer-web">www.lotusgarden-centre.org</p><p class="footer-zh">莲花园共修</p><p class="footer-tagline">May all beings find peace together</p></footer>
</section>

<section class="banner">
  <div class="banner-field"></div>
  <div class="text-panel"></div>
  <svg class="header-tab" viewBox="0 0 70 44" aria-hidden="true"><polygon points="0,0 70,0 70,30 36,30 24,42 12,30 0,30" fill="var(--maroon)"/></svg>
  <div class="org-name">Lotus Garden</div>
  <h1 class="title-zh">十个口解</h1><h2 class="title-en">Ten Mistaking</h2>
  <div class="verse verse-tibetan"><p>ཆོས་ཀྱི་སྒོ་འབྱེད་པ།</p><p>སེམས་ཅན་ཀུན་ལ་བྱམས།</p><p>བློ་སྦྱོང་ཚིག་བཅད་པ།</p><p>ཞི་བའི་ལམ་ལ་འཇུག</p><p>བརྩོན་འགྲུས་རྟག་ཏུ་བསྐྱེད།</p><p>དགེ་བ་ཀུན་ལ་བསྔོ།</p></div>
  <div class="verse verse-chinese"><p>心念安住于正道中</p><p>善言开启众生之门</p><p>错误见解应当放下</p><p>耐心倾听慈悲增长</p><p>明见带来日常安宁</p><p>精进不懈远离骄慢</p><p>思维而后方可行事</p></div>
  <div class="verse verse-notes"><p>一、心念清净不散乱</p><p>二、功德回向一切众生</p></div>
  <div class="verse verse-english"><p>Mind at ease we walk the path today.</p><p>Kind words open the door to others.</p><p>Each mistaken view may be gently set aside.</p><p>Patience grows when we listen with care.</p><p>Clear seeing brings calm to daily life.</p><p>Let effort be steady and free of pride.</p><p>Study and reflect before we choose to act.</p><p>Share the merit with every living being.</p></div>
  <footer class="footer-band"><p class="footer-web">www.lotusgarden-centre.org</p><p class="footer-zh">莲花园共修</p><p class="footer-tagline">May all beings find peace together</p></footer>
</section>

</main>
</body>
</html>
```